PowerPoint Design for TALLY Polls

TALLY Polls stands for 'Tracking Attitudes Linked Lately Yearly Polls'. It is a collaborative research effort to format and combine multiple sources of public opinion data from around the world into merged datasets. We need a Microsoft PowerPoint design for our conference/workshop presentations and instructional videos used as part of our research efforts and crowdsourced development. The design should match the website design and logo, which are attached to this contest (these are the files from previous successful design contests).

Slides will contain a lot of data visualizations, tables with statistical output (lots of numbers), and figures. Bullet points will be used frequently on slides and larg blocks of text should be avided. Margins should be narrow to maximize space used and the size of fonts must be large enough (24-32+) to be visible at the back of classrooms and conference rooms.
Updates

I was away at a conference and am now busy with teaching preparation, so I need a few extra days to give adequate feedback.

Target Market(s)

academia, government, non-profits, postgraduates, researchers

Font styles to use
Sans Serif

Colors

Designer to choose colors to be used in the design.

Requirements
Must have
• designs for common slide layouts
Nice to have
• thematic link with website design and logo

```html
<!DOCTYPE html>
<html lang="en">
<head>
<meta charset="utf-8">
<title>TALLY Polls – How We Work</title>
<link href="https://fonts.googleapis.com/css2?family=Open+Sans:wght@400;600;700&display=swap" rel="stylesheet">
<style>
  :root {
    --brand-blue: #1a6cad;
    --title-blue: #1b6eb0;
    --manager-blue: #2d80c2;
    --director-blue: #2a6a9e;
    --controller-blue: #4cc0f0;
    --body-grey: #9a9a9a;
    --paper: #ffffff;
    --photo-light: #c9ccce;
    --photo-dark: #7b8187;
  }
  * { margin: 0; padding: 0; box-sizing: border-box; }
  html, body { width: 1200px; height: 900px; overflow: hidden; background: var(--paper); }
  body { font-family: "Open Sans", Arial, sans-serif; }

  .slide { position: relative; width: 1200px; height: 900px; background: var(--paper); overflow: hidden; }

  .photo-strip {
    position: absolute; left: 0; top: 0; width: 232px; height: 900px;
    background: linear-gradient(160deg, var(--photo-light) 0%, #a9adb1 45%, var(--photo-dark) 100%);
  }

  .slide-title {
    position: absolute; left: 274px; top: 108px;
    color: var(--title-blue); font-weight: 700; font-size: 50px; line-height: 60px;
  }

  .content { position: absolute; left: 277px; top: 262px; width: 330px; }
  .subtitle { color: var(--title-blue); font-weight: 700; font-size: 23px; line-height: 34px; margin-bottom: 10px; }
  .body-copy { color: var(--body-grey); font-size: 19.5px; line-height: 33px; }

  .roles { position: absolute; left: 640px; top: 205px; width: 480px; height: 450px; }
  .roles text { font-family: "Open Sans", Arial, sans-serif; fill: #ffffff; text-anchor: middle; }
  .role-name { font-weight: 700; font-size: 25px; }
  .role-desc { font-size: 17px; }

  .footer-band { position: absolute; left: 232px; top: 856px; width: 653px; height: 34px; background: var(--brand-blue); }

  .brand { position: absolute; left: 906px; top: 850px; display: flex; align-items: center; gap: 10px; }
  .brand-dot { width: 26px; height: 26px; border-radius: 50%; background: var(--brand-blue); }
  .brand-name { color: var(--brand-blue); font-weight: 600; font-size: 27px; line-height: 40px; }
</style>
</head>
<body>
<main class="slide">
  <div class="photo-strip" role="img" aria-label="Photo of a group of people standing on a concrete floor, seen from above, one woman smiling up at the camera"></div>

  <h1 class="slide-title">How<br>We Work</h1>

  <section class="content">
    <h2 class="subtitle">Subtext Title Here</h2>
    <p class="body-copy">Contributes to the eradication of extreme poverty by partnering with governments and global agencies to ensure that, through policy and practice, they effectively serve people living in conditions of extreme poverty and vulnerability</p>
    <p class="body-copy">Contributes to the eradication of extreme poverty by partnering with governments and global agencies to ensure that, through policy and practice, they effectively serve people living in conditions of extreme poverty and vulnerability</p>
  </section>

  <svg class="roles" viewBox="640 205 480 450" aria-label="Role diagram: Manager, Director, Controller">
    <circle cx="870" cy="333" r="120" fill="var(--manager-blue)"/>
    <circle cx="768" cy="518" r="120" fill="var(--director-blue)" fill-opacity="0.95"/>
    <circle cx="984" cy="518" r="120" fill="var(--controller-blue)" fill-opacity="0.92"/>

    <text class="role-name" x="870" y="279">Manager</text>
    <text class="role-desc" x="870" y="313">Contributes to the</text>
    <text class="role-desc" x="870" y="341">eradication of extreme</text>
    <text class="role-desc" x="870" y="369">poverty by partnering</text>

    <text class="role-name" x="760" y="476">Director</text>
    <text class="role-desc" x="760" y="510">Contributes to the</text>
    <text class="role-desc" x="760" y="538">eradication of extreme</text>
    <text class="role-desc" x="760" y="566">poverty by partnering</text>

    <text class="role-name" x="995" y="476">Controller</text>
    <text class="role-desc" x="995" y="510">Contributes to the</text>
    <text class="role-desc" x="995" y="538">eradication of extreme</text>
    <text class="role-desc" x="995" y="566">poverty by partnering</text>
  </svg>

  <div class="footer-band"></div>
  <div class="brand">
    <span class="brand-dot"></span>
    <span class="brand-name">TALLY Polls</span>
  </div>
</main>
</body>
</html>
```